Business Card Design Project

Refresh of logo attached. Require text underneath to be more ledgible, crisper & cleaner.

Overall, staying with same colour scheme need a brighter, crisper, easily readible business card style.

Industry/Entity Type

Business

```html
<!DOCTYPE html>
<html lang="en">
<head>
<meta charset="utf-8">
<title>NORVEX Business Card</title>
<link rel="stylesheet" href="https://fonts.googleapis.com/css2?family=Open+Sans:wght@400;600&family=Tinos:wght@400&display=swap">
<style>
  :root {
    --backdrop: #e9e9e9;
    --card: #ffffff;
    --ink: #111111;
    --teal: #2e7f9e;
    --teal-dark: #2a5566;
    --rule: #7a7a7a;
  }
  * { margin: 0; padding: 0; box-sizing: border-box; }
  html, body { width: 1200px; height: 533px; overflow: hidden; }
  body { background: var(--backdrop); position: relative; }

  .card {
    position: absolute;
    top: 88px;
    width: 508px;
    height: 305px;
    background: var(--card);
    box-shadow: 0 2px 8px rgba(0,0,0,0.18);
  }
  .card--front { left: 83px; }
  .card--back { left: 640px; }

  .chevron-band {
    position: absolute;
    height: 24px;
    background: linear-gradient(90deg, var(--teal-dark), var(--teal));
  }
  .chevron-band--top { left: 373px; top: 19px; width: 117px; }
  .chevron-band--bottom { left: 18px; top: 261px; width: 115px; }

  .brand {
    position: absolute;
    display: flex;
    align-items: center;
    gap: 10px;
  }
  .brand__mark { width: 14px; height: 14px; background: var(--teal); }
  .brand__name {
    font-family: "Open Sans", sans-serif;
    font-weight: 600;
    font-size: 32px;
    line-height: 1;
    color: var(--ink);
  }
  .card--front .brand { left: 50px; top: 152px; }
  .card--back .brand { left: 168px; top: 152px; }

  .divider {
    position: absolute;
    left: 265px;
    top: 139px;
    width: 2px;
    height: 146px;
    background: var(--rule);
  }

  .person { position: absolute; left: 273px; top: 132px; }
  .person__name {
    font-family: "Open Sans", sans-serif;
    font-weight: 600;
    font-size: 20px;
    color: var(--ink);
    line-height: 1.2;
  }
  .person__title {
    font-family: "Open Sans", sans-serif;
    font-size: 13px;
    color: var(--teal);
    line-height: 1.3;
  }
  .contact {
    list-style: none;
    margin-top: 12px;
    margin-left: 6px;
    font-family: "Tinos", serif;
    font-size: 12.5px;
    color: var(--ink);
    line-height: 1.35;
  }
  .website {
    position: absolute;
    right: 36px;
    top: 268px;
    font-family: "Open Sans", sans-serif;
    font-size: 14px;
    color: var(--ink);
  }
</style>
</head>
<body>
  <section class="card card--front">
    <div class="chevron-band chevron-band--top" role="img" aria-label="Row of teal chevron arrows"></div>
    <div class="brand">
      <span class="brand__mark"></span>
      <span class="brand__name">NORVEX</span>
    </div>
    <div class="divider"></div>
    <div class="person">
      <p class="person__name">Daniel R. Whitford</p>
      <p class="person__title">Certified Executor Advisor</p>
      <ul class="contact">
        <li>T : (555) 010 4821</li>
        <li>M : (555) 010 7390</li>
        <li>E : daniel@norvex.ca</li>
      </ul>
    </div>
    <p class="website">www.norvex.ca</p>
    <div class="chevron-band chevron-band--bottom" role="img" aria-label="Row of teal chevron arrows"></div>
  </section>

  <section class="card card--back">
    <div class="brand">
      <span class="brand__mark"></span>
      <span class="brand__name">NORVEX</span>
    </div>
  </section>
</body>
</html>
```